Eye catching Bottle label for pink gin targeting women 25+

We need a new label for a re-launch of our shimmering strawberry pink gin liqueur. We would like it to look premium and eye catching on the shelf. We have 2 labels we require, one for 200ml bottle (2x2 inches) and one for 500ml bottle 4x4 inches). Label must state the ml of the bottle abd that it is 18.75%Vol. Also say Shimmering Strawberry Gin Liqueur with the brand name at the top - Harlow Vale Distillers. We have a logo but it doesn't need to be used if it doesn't work with the design/colours. The gin is presented in a clear bottle and is pink and sparkly. See uploaded image for reference.

Target Market(s)

Women aged 25-45

Font styles to use
Decorative

Colors
f59296
fbd4d5
eea4c8

Requirements
Must have
• Bottle size - 500ml/200ml
• Must say 18.75% Vol
• Must have brand name - Harlow Vale Distillers
• Must have product name - Shimmering Pink Strawberry
• Must say - Gin Liqueur
Nice to have
• Some sort of floral or swirley background detail would be nice
Should not have
• Must not appeal to children

```html
<!DOCTYPE html>
<html lang="en">
<head>
<meta charset="UTF-8">
<title>Harlow Vale Distillers – Pink Gin Liqueur Label</title>
<link rel="stylesheet" href="https://fonts.googleapis.com/css2?family=Pinyon+Script&family=IM+Fell+English+SC&family=Roboto:wght@400;700&family=Oswald:wght@500&display=swap">
<style>
  :root {
    --blush-light: #fdf1f4;
    --blush: #fbd4d5;
    --rose: #f59296;
    --orchid: #eea4c8;
    --crimson: #c8334e;
    --crimson-deep: #a8223b;
    --ink: #1f1a1c;
    --charcoal: #2e2629;
    --white: #ffffff;
  }
  html, body {
    margin: 0;
    padding: 0;
    overflow: hidden;
    background: var(--white);
  }
  .label {
    position: relative;
    width: 1200px;
    height: 1200px;
    overflow: hidden;
    background: linear-gradient(180deg, #f9dbe4 0%, var(--blush-light) 38%, #fbe3ea 62%, #f7c7d6 100%);
  }
  .blossom {
    position: absolute;
  }
  .blossom--top {
    left: 0;
    top: 60px;
    width: 520px;
    height: 380px;
    background: radial-gradient(ellipse at 30% 45%, rgba(244,170,190,0.55) 0%, rgba(250,210,222,0.35) 45%, rgba(253,241,244,0) 75%);
  }
  .blossom--bottom {
    left: 0;
    top: 640px;
    width: 1200px;
    height: 420px;
    background:
      radial-gradient(ellipse at 18% 55%, rgba(240,150,175,0.7) 0%, rgba(246,190,208,0.35) 35%, rgba(253,241,244,0) 60%),
      radial-gradient(ellipse at 82% 50%, rgba(240,150,175,0.7) 0%, rgba(246,190,208,0.35) 35%, rgba(253,241,244,0) 60%),
      radial-gradient(ellipse at 50% 80%, rgba(238,164,200,0.45) 0%, rgba(253,241,244,0) 55%);
  }
  .swoosh {
    position: absolute;
    left: 0;
    top: 0;
  }
  .brand {
    position: absolute;
    left: 0;
    top: 150px;
    width: 1200px;
    text-align: center;
    font-family: "Pinyon Script", cursive;
    font-size: 118px;
    line-height: 130px;
    color: var(--ink);
  }
  .product {
    position: absolute;
    left: 0;
    top: 540px;
    width: 1200px;
    text-align: center;
    font-family: "IM Fell English SC", serif;
    font-size: 168px;
    line-height: 1;
    letter-spacing: 6px;
    color: var(--crimson);
    margin: 0;
    font-weight: 400;
  }
  .category {
    position: absolute;
    left: 0;
    top: 728px;
    width: 1200px;
    text-align: center;
    font-family: "IM Fell English SC", serif;
    font-size: 62px;
    line-height: 1;
    letter-spacing: 4px;
    color: var(--crimson);
  }
  .footer-band {
    position: absolute;
    left: 0;
    bottom: 0;
  }
  .volume {
    position: absolute;
    left: 75px;
    top: 999px;
    width: 240px;
    height: 57px;
    background: var(--crimson-deep);
    color: var(--white);
    font-family: "Roboto", sans-serif;
    font-size: 40px;
    line-height: 57px;
    text-align: center;
  }
  .flavour {
    position: absolute;
    left: 324px;
    top: 1014px;
    width: 525px;
    height: 162px;
    box-sizing: border-box;
    border: 8px solid var(--crimson);
    background: var(--charcoal);
    color: var(--white);
    font-family: "Oswald", sans-serif;
    font-weight: 500;
    font-size: 56px;
    line-height: 64px;
    letter-spacing: 3px;
    text-align: center;
    display: flex;
    flex-direction: column;
    justify-content: center;
  }
  .abv {
    position: absolute;
    left: 879px;
    top: 1050px;
    width: 237px;
    height: 60px;
    background: var(--crimson-deep);
    color: var(--white);
    font-family: "Roboto", sans-serif;
    font-size: 34px;
    line-height: 60px;
    text-align: center;
  }
</style>
</head>
<body>
  <main class="label">
    <div class="blossom blossom--top" role="img" aria-label="Soft pink cherry blossom branch"></div>
    <div class="blossom blossom--bottom" role="img" aria-label="Cherry blossom flowers in full bloom"></div>

    <svg class="swoosh" width="1200" height="200" viewBox="0 0 1200 200" aria-hidden="true">
      <path d="M0 0 H1200 V40 C900 20 620 60 360 80 C200 92 80 96 0 110 Z" fill="var(--charcoal)"/>
      <path d="M620 0 H1200 V150 C1100 80 980 60 820 70 C740 74 680 50 620 0 Z" fill="var(--crimson)"/>
      <path d="M760 0 H1200 V90 C1100 40 960 30 860 34 C810 36 780 20 760 0 Z" fill="var(--rose)" opacity="0.85"/>
      <path d="M0 110 C120 96 260 92 420 78 C300 110 140 130 0 150 Z" fill="var(--orchid)" opacity="0.5"/>
    </svg>

    <div class="brand">Harlow Vale<br>Distillers</div>

    <h1 class="product">PINK GIN</h1>
    <div class="category">LIQUEUR</div>

    <svg class="footer-band" width="1200" height="180" viewBox="0 0 1200 180" aria-hidden="true">
      <path d="M0 70 C300 40 700 110 1200 60 V180 H0 Z" fill="var(--rose)" opacity="0.55"/>
      <path d="M0 120 C320 90 760 150 1200 110 V180 H0 Z" fill="var(--crimson)"/>
    </svg>

    <div class="volume">500 ml</div>
    <div class="flavour"><span>SHIMMERING</span><span>STRAWBERRY</span></div>
    <div class="abv">18,75% Vol</div>
  </main>
</body>
</html>
```